AMBER AND STONE WEB

We need a home design in wordpress, we have now a web but we would like to improve it. Our current web is www.amberandstonevillas.example Our business is holliday rental of villas in Ibiza. Our guest must know that we are a reliable company, professional and with experience and good reviews. We want them to click in our reservation engine: https://bookings.amberandstonevillas.example/en/ and make reservation in our website. We would also like to say that all the properties that we have are just us who commercialize so we have best price available. Many people are going to see our villas in staylister.example and look to our website to make a reservation with us so we need to show them that they are at the right place and click at our link to our reservation engine. What make us special is that we are a local company, we are from Ibiza, Our guests are always received in person by the Amber and Stone Villas team. You will enjoy extensive tourist information when you check in and during the entire stay. You will be attended by ChatLoop and calls, always happy to help so that you have a happy and fun stay! Our guest stay is better than in hotel as they have more spece, private swiming pool, private garden, barbeque ... To rent a villa is the best way to stay in Ibiza. We also have a promotional video: https://vidshare.example/Qm7tLp2Xz9A Let our philosophy be shown, we think that coming on holiday to Ibiza implies seeing the nature that we have in Ibiza, hence our name AMBER AND STONE, like the pins that almost touch the sea in Ibiza, or the posidonea meadows where the intense green of the seaweed and the blue of the sea. We are aware of the environment, and we love Ibiza. For us, the client who visits Ibiza, should rent a car, go around the island, eat in a restaurant one day in front of the sea, is a night of partying to the discs, go shopping, visit the ancient heritage of Umanity, make some aquatic sport, enjoy the pool, those are for us Ibiza.

Target Market(s)

Europe, people from Holand, UK, Germany, France, Spain ...

Industry/Entity Type

Tourism

Colors

Designer to choose colors to be used in the design.

Requirements
Must have
• Pictures of Ibiza.
Nice to have
• Our name Amber and Stone Villas is beacuse in Ibiza there is forest that almost touch the watter of the Mediterranean sea, so you can see green of the forest and blue of the sea and the sky. And also beacause under the watter of the sea there is a plant called Posidonia that is also green please see the picture of posidonia.

```html
<!DOCTYPE html>
<html lang="en">
<head>
<meta charset="utf-8">
<title>Amber and Stone Villas – Home</title>
<link href="https://fonts.googleapis.com/css2?family=Lato:ital,wght@0,400;0,700;0,900;1,400&display=swap" rel="stylesheet">
<style>
:root{
  --blue:#0f6fc6;
  --blue-dark:#0b4f9e;
  --green:#7a9a2e;
  --ink:#222;
  --muted:#777;
  --light:#f2f2f2;
  --white:#fff;
  --star:#f2c200;
}
*{margin:0;padding:0;box-sizing:border-box}
html,body{width:719px;height:1200px;overflow:hidden;background:#fff}
body{font-family:'Lato',sans-serif;color:var(--ink);position:relative}
.abs{position:absolute}
/* hero */
.hero{left:0;top:0;width:719px;height:273px;background:linear-gradient(180deg,#8fc2ea 0%,#bfe0f0 22%,#3fb4c4 45%,#1c9aa6 70%,#2d6f6a 100%)}
.hero-cliff-l{left:0;top:40px;width:140px;height:233px;background:linear-gradient(90deg,#6b6a3c,#a08a60 70%,rgba(160,138,96,0));}
.hero-cliff-r{right:0;top:50px;width:180px;height:223px;background:linear-gradient(270deg,#5f7a36,#b9934f 60%,rgba(185,147,79,0));}
.topbtn{top:0;height:10px;background:#dfe9f3;font-size:5px;line-height:10px;text-align:center;color:#333}
.nav{left:150px;top:12px;width:420px;height:17px;background:#fff;display:flex;align-items:center;padding:0 6px}
.brand{font-size:8px;color:var(--green);font-weight:700;letter-spacing:.3px;display:flex;align-items:center;gap:4px}
.brand i{width:6px;height:6px;border-radius:50%;background:var(--green);display:block}
.menu{margin-left:auto;display:flex;gap:8px;font-size:5.4px;color:#555}
.menu .on{color:var(--blue);border-bottom:1px solid var(--blue);padding-bottom:2px}
.hero-title{left:0;top:84px;width:719px;text-align:center;color:#fff;font-weight:900;font-size:24px;line-height:28px;text-shadow:0 1px 3px rgba(0,0,0,.35)}
.search{left:175px;top:192px;width:370px;height:30px;background:rgba(220,240,245,.85);}
.field label{display:block;font-size:4.2px;color:#333;margin-bottom:2px}
.field div{background:#fff;height:13px;font-size:4.6px;line-height:13px;padding-left:4px;color:#333}
.search-btn{left:477px;top:197px;width:61px;height:20px;background:var(--blue);color:#fff;font-weight:700;font-size:7px;line-height:20px;text-align:center}
/* intro */
.intro{left:0;top:273px;width:719px;height:137px;background:var(--light)}
.intro h2{position:absolute;top:17px;width:719px;text-align:center;color:var(--green);font-size:12.5px;font-weight:900}
.intro .lead{position:absolute;top:34px;width:719px;text-align:center;font-size:5.2px;line-height:6.6px;color:#666}
.feature{top:64px;width:110px;text-align:center}
.feature h3{font-size:7px;font-weight:400;color:#444;margin:6px 0 2px}
.feature p{font-size:4.8px;line-height:6.4px;color:#999}
/* villas */
.villas{left:0;top:410px;width:719px;height:150px;background:#fff}
.side-photo{top:20px;width:150px;height:130px;background:linear-gradient(180deg,#dfeef6,#7ab4cf 55%,#e8eef0)}
.villas-text{left:149px;top:15px;width:236px}
.villas-text h2{font-size:8px;font-weight:700;margin-bottom:6px}
.villas-text p{font-size:4.6px;line-height:5.9px;color:#444;margin-bottom:4px}
.collage{left:392px;top:17px;width:178px;height:106px;background:#fff;border:1px solid #ddd}
.ph{position:absolute}
/* video */
.video-band{left:0;top:560px;width:719px;height:140px;background:linear-gradient(180deg,#b9dcea,#8ed0dc 50%,#bfe2e4)}
.video-title{left:0;top:571px;width:719px;text-align:center;font-size:8.5px;font-weight:700}
.video{left:215px;top:591px;width:290px;height:152px;background:linear-gradient(160deg,#2b6cb4,#6fa8dc 45%,#1c3c5e 75%,#153045)}
.video-bar{left:215px;top:734px;width:290px;height:9px;background:rgba(0,0,0,.75)}
/* rooms */
.room{top:773px;width:134px}
.room .img{height:87px;border:3px solid #fff;outline:1px solid #ddd}
.room h3{position:absolute;top:93px;left:0;font-size:8px;font-weight:700}
.room .price{position:absolute;top:93px;right:0;font-size:8px;font-weight:700;text-align:right}
.room .price small{display:block;font-size:3.6px;font-weight:400;color:#777;margin-top:-1px}
.room p{position:absolute;top:107px;left:0;width:134px;font-size:4.6px;line-height:6px;color:#555}
.book{position:absolute;top:133px;left:0;width:58px;height:13px;background:var(--blue);color:#fff;font-size:4.8px;line-height:13px;text-align:center}
/* testimonial */
.review{left:0;top:942px;width:719px;height:172px;background:linear-gradient(120deg,#e9eef2,#f6f5f3 50%,#e6e2dd)}
.avatar{left:334px;top:962px;width:52px;height:52px;border-radius:50%;background:linear-gradient(#d8b89a,#8a6b55);border:2px solid #8aa53a}
.quote{left:190px;top:1025px;width:340px;text-align:center;font-style:italic;font-size:5.3px;line-height:7px;color:#333}
.rule{left:348px;top:1048px;width:24px;height:1px;background:var(--green)}
.name{left:0;top:1055px;width:719px;text-align:center;font-size:5.8px;color:var(--blue)}
.stars{left:0;top:1063px;width:719px;text-align:center;font-size:7px;color:var(--star);letter-spacing:1px}
.dots{left:350px;top:1086px;display:flex;gap:2px}
.dots i{width:4px;height:4px;border:1px solid var(--green);border-radius:50%;display:block}
.dots i.on{background:var(--green)}
/* footer */
.footer{left:0;top:1114px;width:719px;height:86px;background:var(--blue-dark)}
.foot-badge{left:347px;top:1102px;width:26px;height:26px;border-radius:50%;background:var(--blue-dark)}
.foot-name{left:0;top:1131px;width:719px;text-align:center;color:#fff;font-size:9px;letter-spacing:.8px}
.contact{top:1154px;display:flex;align-items:center;gap:5px;color:#fff;font-size:5.8px}
.contact span{border-bottom:1px solid #fff;padding-bottom:1px}
.contact i{width:11px;height:11px;border-radius:50%;background:#fff;display:flex;align-items:center;justify-content:center}
.foot-line{left:0;top:1180px;width:719px;height:1px;background:rgba(255,255,255,.25)}
.copy{left:0;top:1186px;width:719px;text-align:center;color:#fff;font-size:4.8px}
</style>
</head>
<body>

<section class="abs hero" role="img" aria-label="Photo of an Ibiza bay with turquoise water, cliffs and a sailing boat"></section>
<div class="abs hero-cliff-l" aria-hidden="true"></div>
<div class="abs hero-cliff-r" aria-hidden="true"></div>

<div class="abs topbtn" style="left:487px;width:32px">BOOK</div>
<div class="abs topbtn" style="left:521px;width:49px">ALL PROPERTIES</div>
<header class="abs nav">
  <div class="brand"><i></i>AMBER AND STONE</div>
  <nav class="menu"><span class="on">HOME</span><span>EXPERIENCE</span><span>ABOUT US</span><span>CONTACT US</span></nav>
</header>

<h1 class="abs hero-title">THE BEST WAY TO<br>STAY IN IBIZA!</h1>

<form class="abs search">
  <div class="abs field" style="left:5px;top:4px;width:112px"><label>Check-in and check-out date:</label><div>4 May 2019 - 10 May 2019</div></div>
  <div class="abs field" style="left:120px;top:4px;width:26px"><label>Nights:</label><div>4</div></div>
  <div class="abs field" style="left:151px;top:4px;width:108px"><label>No. of guests and rooms:</label><div>4 adults + 1 child (1 room)</div></div>
  <div class="abs field" style="left:265px;top:4px;width:30px"><label>Promo Code:</label><div>4</div></div>
</form>
<div class="abs search-btn">SEARCH</div>

<section class="abs intro">
  <h2>WE LOVE IBIZA HOLIDAY!</h2>
  <p class="lead">We deem worthy of them, and they are accusing those who hate the righteous,<br>But, in truth, and the blandishments of current events.</p>
  <div class="abs feature" style="left:182px">
    <svg width="22" height="20" viewBox="0 0 22 20" fill="none" stroke="#0f6fc6" stroke-width="1"><path d="M3 9 L11 2 L19 9 V18 H3 Z"/><rect x="6" y="12" width="10" height="4"/><path d="M6 12 V10 H16 V12"/></svg>
    <h3>Cozy and charming rooms</h3>
    <p>Lorem ipsum dolor sit amet, consectetur adipiscing elit, sed tempor and vitality, so that the labor and sorrow.</p>
  </div>
  <div class="abs feature" style="left:305px">
    <svg width="22" height="20" viewBox="0 0 22 20" fill="none" stroke="#0f6fc6" stroke-width="1"><path d="M3 7 Q10 0 17 7 Z"/><path d="M10 6 V17"/><path d="M5 17 H19 L16 12 H9"/></svg>
    <h3>Relax in a beautiful contest</h3>
    <p>Lorem ipsum dolor sit amet, consectetur adipiscing elit, sed tempor and vitality, so that the labor and sorrow.</p>
  </div>
  <div class="abs feature" style="left:428px">
    <svg width="22" height="20" viewBox="0 0 22 20" fill="none" stroke="#0f6fc6" stroke-width="1"><circle cx="8" cy="5" r="2"/><circle cx="14" cy="6" r="2"/><path d="M4 2 L8 9 L12 2 M10 3 L14 10 L18 3 M6 18 V10 H10 V18 M12 18 V11 H16 V18"/></svg>
    <h3>Enjoy country side activities</h3>
    <p>Lorem ipsum dolor sit amet, consectetur adipiscing elit, sed tempor and vitality, so that the labor and sorrow.</p>
  </div>
</section>

<section class="abs villas">
  <div class="abs side-photo" style="left:0" role="img" aria-label="Photo of a family walking in the sea waves"></div>
  <div class="abs side-photo" style="right:0" role="img" aria-label="Photo of a family walking in the sea waves"></div>
  <div class="abs villas-text">
    <h2>VILLAS AND THE COUNTRYSIDE <span style="font-weight:400">The best option to stay in Ibiza</span></h2>
    <p>Amber and Stone Villas Ibiza is a company specialized in offering its clients accommodation in Villas on the countryside of Ibiza. Our guests enjoy the rural Ibiza, tranquility, relax, private pool, close to dream beaches and coves, the best restaurants, an unforgettable holiday for family or friends.</p>
    <p>Every day can be a different experience, beach, restaurant, flea market, disco, hiking, kayaking, horseback riding, shopping, history, boat ride! There is a lot of variety for all budgets!</p>
    <p>The maximum distances of the island are 41 kilometers from north to south and 15 kilometers from east to west, we always recommend renting a car. Enjoy the freedom to go where you prefer, without depending on schedules or public transportation.</p>
    <p>Each client is different, both for those who discover Ibiza for the first time and for those who have already been many times, it is a pleasure for us to share our favorite places with our guests and help them to make their experience very special.</p>
  </div>
  <div class="abs collage">
    <div class="ph" style="left:2px;top:2px;width:69px;height:101px;background:linear-gradient(180deg,#3a86d0,#8fbde0 55%,#b8b2a4)" role="img" aria-label="Photo of a stone wall path by the sea"></div>
    <div class="ph" style="left:74px;top:2px;width:102px;height:49px;background:linear-gradient(180deg,#9ab6cc,#6f8ea6 60%,#3d5a44)" role="img" aria-label="Photo of rocky islet off the Ibiza coast"></div>
    <div class="ph" style="left:74px;top:54px;width:102px;height:49px;background:linear-gradient(180deg,#3d8fd0,#e0a23a 55%,#2f6b8a)" role="img" aria-label="Photo of golden cliffs above a blue cove"></div>
  </div>
</section>

<section class="abs video-band" role="img" aria-label="Photo of a white sand beach with turquoise sea and pine trees"></section>
<h2 class="abs video-title">Our Video</h2>
<div class="abs video" role="img" aria-label="Promotional video still of waves breaking on dark rocks"></div>
<div class="abs video-bar">
  <div class="abs" style="left:2px;top:1px;width:286px;height:1px;background:#666"></div>
  <div class="abs" style="left:2px;top:1px;width:64px;height:1px;background:#e00"></div>
  <svg class="abs" style="left:5px;top:3px" width="5" height="5" viewBox="0 0 5 5"><path d="M0 0 L5 2.5 L0 5 Z" fill="#fff"/></svg>
</div>

<article class="abs room" style="left:149px">
  <div class="img" role="img" aria-label="Photo of a single room with wooden headboard"style="background:linear-gradient(180deg,#c9a27c,#8a6446 55%,#d8d4cf)"></div>
  <h3>Single Rooms</h3><div class="price">$ 90<small>Per night</small></div>
  <p>Lorem ipsum dolor sit amet, consectetur adipiscing elit, sed tempor and vitality, so that the labor and sorrow, some important things to do eiusmod.</p>
  <div class="book">Book Now</div>
</article>
<article class="abs room" style="left:292px">
  <div class="img" role="img" aria-label="Photo of a double room with dark headboard and white bedding" style="background:linear-gradient(180deg,#4a2e22,#7a5844 45%,#ecebe8)"></div>
  <h3>Double rooms</h3><div class="price">$ 130<small>Per night</small></div>
  <p>Lorem ipsum dolor sit amet, consectetur adipiscing elit, sed tempor and vitality, so that the labor and sorrow, some important things to do eiusmod.</p>
  <div class="book">Book Now</div>
</article>
<article class="abs room" style="left:435px">
  <div class="img" role="img" aria-label="Photo of a king double room with green throw" style="background:linear-gradient(180deg,#5c6470,#e8e6e0 50%,#9ccf2e 75%,#6a6a6a)"></div>
  <h3>King Double rooms</h3><div class="price">$ 150<small>Per night</small></div>
  <p>Lorem ipsum dolor sit amet, consectetur adipiscing elit, sed tempor and vitality, so that the labor and sorrow, some important things to do eiusmod.</p>
  <div class="book">Book Now</div>
</article>

<section class="abs review" role="img" aria-label="Faint photo of hands typing on a laptop"></section>
<div class="abs avatar" role="img" aria-label="Portrait photo of the reviewer"></div>
<p class="abs quote">Lorem Ipsum is simply dummy text of the printing and typesetting industry. Lorem Ipsum has been the industry's standard dummy text ever since the 1500s, when an unknown printer took a galley of type andLorem Ipsum is simply dummy text of the printing</p>
<div class="abs rule"></div>
<div class="abs name">Daniel Harwick</div>
<div class="abs stars">★★★★★</div>
<div class="abs dots"><i></i><i></i><i class="on"></i><i></i></div>

<footer class="abs footer"></footer>
<div class="abs foot-badge"></div>
<div class="abs foot-name">AMBER AND STONE</div>
<div class="abs contact" style="left:149px">
  <i><svg width="6" height="5" viewBox="0 0 6 5"><rect x=".5" y=".5" width="5" height="4" fill="none" stroke="#0b4f9e" stroke-width=".8"/><path d="M.5 .5 L3 3 L5.5 .5" fill="none" stroke="#0b4f9e" stroke-width=".8"/></svg></i>
  <span>reservas@amberandstonevillas.example</span>
</div>
<div class="abs contact" style="left:330px">
  <i><svg width="6" height="6" viewBox="0 0 6 6"><path d="M1 .5 L2.3 .5 L2.8 2 L2 2.6 Q2.7 3.6 3.4 4 L4 3.2 L5.5 3.7 L5.5 5 Q2.5 5.3 .6 1.5 Z" fill="#0b4f9e"/></svg></i>
  <span>+34600481257</span>
</div>
<div class="abs contact" style="left:453px">
  <i><svg width="6" height="7" viewBox="0 0 6 7"><path d="M3 .3 A2.4 2.4 0 0 1 5.4 2.7 C5.4 4.3 3 6.7 3 6.7 C3 6.7 .6 4.3 .6 2.7 A2.4 2.4 0 0 1 3 .3 Z" fill="#0b4f9e"/><circle cx="3" cy="2.7" r=".9" fill="#fff"/></svg></i>
  <span>27, Camí de Sa Pinada, 07999, Ibiza</span>
</div>
<div class="abs foot-line"></div>
<div class="abs copy">©2019 All rights reserved</div>

</body>
</html>
```